Corvelle Matchmaking - Innovative AI-based Online Dating App

Hello, I am creating a new online dating app that subsumes the personalization and compatibility analysis of human matchmaking, but is combined with the convenience of modern dating apps such as brisket. The app is called Corvelle.

There is a lot of pain and fatigue in modern online dating. Corvelle uses a concise but effective questionnaire that is combined with cutting-edge AI, social psychology research, and psycholinguistic modelling to effectively and conveniently find dating matches with real compatibility - as opposed to any major app on the market. A personalized introduction for every user is generated everyday to introduce you to a new potential match - this introduction is totally unique and will never be seen before or again. The introduction is intertwined with the user’s images to create an attractive “newsletter” feel.

"Corvelle" is Italian for lagoon, which is "a shallow body of water protected from a larger body of water (usually the ocean) by sandbars, barrier islands, or coral reefs." Lagoons are beautiful, tropical, lush watery paradises - as I see it. This is meant to be the inspiration for the feel, color scheme and design of the app.

To that end, I have included concept images of lagoons to evoke the feeling of a paradise getaway where one may meet their soulmate. This is the feeling I would like to convey with the minimalist app design this product needs to compete.

I have included screenshots of the current app UI. There is a screen for
1) potential matches and incoming likes (just like Brisket) with a logo at the top. There are “Like”, “Dislike”, “Super Like”, and “Super Dislike” buttons that float over the screen as it scrolls. These button shape/colors likely need to change to match the rest of the design
2) Overview of message threads with each match
3) View of message threads
4) Settings page

I would like
1) the logo/header image to be redone (as well as the like/dislike/super like/super dislike buttons to be redone to match the new design)
2) icons for the 4 pages in the bottom navigation bar to be redone
3) color scheme to be optimized and evoking of the desired paradise but professional feeling of a hyper-intelligent (but also empathetic) matchmaker
4) design for the settings screen (to look professional and competitive with other dating apps)

The color scheme /layout/spacing/font(s) for the bubbles on the screen where new potential matches are introduced is the most important part of the design I’m looking for. It’s currently a stack of rounded rectangles basically, but I’m open to all ideas to make this app look as professional as possible while conveying the desired elegance, empathy, and uniqueness of the brand.

Thank you!

Target Market(s)

Single men and women ages 20 - 45

Industry/Entity Type

Online dating / Matchmaking

Requirements
Must have
• For the main screen where new users are being introduced (i.e. the "swipe" page on most dating apps) - some amount of matchmaking introductory text MUST be shown above the user's first profile picture, as indicated in the current screenshots.
Nice to have
• Re-designs of the top "Corvelle" logo/emblem would be nice. If changing the logo, some emblem or graphic in addition to just the text of "Corvelle" would be nice. (Like the way "plumway" has its red flame emblem)
Should not have
• The main "swipe" page should not look identical to other dating apps in the sense of being >90% just a user's first dating profile image. The competitive edge to this app is the user-to-user specific matchmaking introductory text, so some of that must be visible before a user scrolls down for further profile information.

```html
<!DOCTYPE html>
<html lang="en">
<head>
<meta charset="utf-8">
<title>Corvelle – Daily Introduction</title>
<link rel="stylesheet" href="https://fonts.googleapis.com/css2?family=Poppins:wght@300;400;500;600&display=swap">
<style>
  :root {
    --canvas: #ffffff;
    --screen: #f6f7f9;
    --card: #ffffff;
    --ink-soft: #8a8b90;
    --logo: #8d8e93;
    --name-blue: #8bbcf0;
    --teal: #8fdccb;
    --icon-dark: #55565b;
    --nav: #5d5e62;
    --nav-icon: #ffffff;
  }
  * { box-sizing: border-box; margin: 0; padding: 0; }
  html, body {
    width: 1200px; height: 1200px; overflow: hidden;
    background: var(--canvas);
    font-family: "Poppins", sans-serif;
  }
  .app-screen {
    position: absolute; left: 350px; top: 10px;
    width: 500px; height: 1180px;
    background: var(--screen);
    border-radius: 48px;
    overflow: hidden;
    box-shadow: 0 0 0 1px #e6e7ea;
  }
  .brand {
    position: absolute; top: 62px; left: 0; width: 100%;
    text-align: center;
    font-weight: 500; font-size: 66px; line-height: 1;
    color: var(--logo); letter-spacing: -1px;
  }
  .intro-card {
    position: absolute; left: 6px; top: 149px;
    width: 483px; height: 421px;
    background: var(--card);
    border-radius: 24px;
    box-shadow: 0 4px 14px rgba(0,0,0,0.06);
    padding: 34px 14px 0 16px;
    color: var(--ink-soft);
    font-weight: 300; font-size: 20.5px; line-height: 34px;
  }
  .intro-card .greeting { margin-bottom: 4px; }
  .intro-card .recipient { color: var(--name-blue); font-weight: 600; }
  .intro-card .line { display: block; white-space: nowrap; }
  .match-photo {
    position: absolute; left: 8px; top: 603px;
    width: 481px; height: 500px;
    border-radius: 22px 22px 0 0;
    background: linear-gradient(160deg, #5f7a5a 0%, #8c9a86 35%, #b5a7a6 65%, #7b5f63 100%);
  }
  .action-rail {
    position: absolute; left: 401px; top: 677px;
    width: 99px; height: 390px;
    background: #ffffff;
    border-radius: 32px 0 0 32px;
  }
  .action-rail svg { position: absolute; left: 26px; width: 48px; height: 48px; }
  .action-like { top: 47px; }
  .action-superlike { top: 128px; }
  .action-dislike { top: 213px; }
  .action-superdislike { top: 294px; }
  .bottom-nav {
    position: absolute; left: 0; bottom: 0;
    width: 100%; height: 88px;
    background: var(--nav);
  }
  .bottom-nav svg { position: absolute; top: 20px; width: 52px; height: 52px; }
  .nav-matches { left: 27px; }
  .nav-dates { left: 155px; }
  .nav-messages { left: 286px; }
  .nav-settings { left: 420px; }
</style>
</head>
<body>
<main class="app-screen">
  <h1 class="brand">Corvelle</h1>

  <section class="intro-card">
    <p class="greeting">Dear <span class="recipient">Dariel,</span></p>
    <p class="intro-text">
      <span class="line">Allow me to introduce you to Mireya,</span>
      <span class="line">a captivatiing woman who possesses</span>
      <span class="line">an enchanting blend of qualities that</span>
      <span class="line">perfectly align with what you seek in a</span>
      <span class="line">partner. her shared interest in creativ-</span>
      <span class="line">ity is just the beginning of the</span>
      <span class="line">profound connection you could share.</span>
      <span class="line">Mireya’s passion for games, docu-</span>
      <span class="line">mentaries, music and writing mirrors</span>
      <span class="line">your own, promising.</span>
    </p>
  </section>

  <div class="match-photo" role="img" aria-label="Profile photo of the introduced match, outdoors with a bicycle under string lights"></div>

  <aside class="action-rail">
    <svg class="action-like" viewBox="0 0 48 48" aria-label="Like"><path d="M7 25 L19 36 L41 13" fill="none" stroke="var(--teal)" stroke-width="7" stroke-linecap="round" stroke-linejoin="round"/></svg>
    <svg class="action-superlike" viewBox="0 0 48 48" aria-label="Super like"><path d="M24 40 L8 24 C3 19 5 9 13 8 C18 7 22 10 24 14 C26 10 30 7 35 8 C43 9 45 19 40 24 Z" fill="none" stroke="var(--teal)" stroke-width="6" stroke-linejoin="round"/></svg>
    <svg class="action-dislike" viewBox="0 0 48 48" aria-label="Dislike"><path d="M10 10 L38 38 M38 10 L10 38" stroke="var(--icon-dark)" stroke-width="7" stroke-linecap="round"/></svg>
    <svg class="action-superdislike" viewBox="0 0 48 48" aria-label="Super dislike"><path d="M12 5 H36" stroke="var(--icon-dark)" stroke-width="5" stroke-linecap="round"/><rect x="9" y="13" width="30" height="32" rx="7" fill="none" stroke="var(--icon-dark)" stroke-width="5"/><path d="M18 20 V30 Q18 36 24 36 Q30 36 30 30 V20" fill="none" stroke="var(--icon-dark)" stroke-width="5" stroke-linecap="round"/></svg>
  </aside>

  <nav class="bottom-nav">
    <svg class="nav-matches" viewBox="0 0 52 52" aria-label="Matches"><circle cx="26" cy="26" r="18" fill="none" stroke="var(--nav-icon)" stroke-width="5"/></svg>
    <svg class="nav-dates" viewBox="0 0 52 52" aria-label="Dates"><path d="M9 6 H37" stroke="var(--nav-icon)" stroke-width="4" stroke-linecap="round"/><path d="M9 15 H37 V32 Q37 44 23 44 Q9 44 9 32 Z" fill="none" stroke="var(--nav-icon)" stroke-width="4.5" stroke-linejoin="round"/><path d="M37 20 H40 Q47 20 47 27 Q47 34 40 34 H36" fill="none" stroke="var(--nav-icon)" stroke-width="4.5"/></svg>
    <svg class="nav-messages" viewBox="0 0 52 52" aria-label="Messages"><path d="M12 7 H34 Q40 7 40 13 V36 L48 44 H12 Q6 44 6 38 V13 Q6 7 12 7 Z" fill="none" stroke="var(--nav-icon)" stroke-width="4.5" stroke-linejoin="round"/><path d="M14 20 H31 M14 30 H31" stroke="var(--nav-icon)" stroke-width="4.5" stroke-linecap="round"/></svg>
    <svg class="nav-settings" viewBox="0 0 52 52" aria-label="Settings"><circle cx="26" cy="26" r="13" fill="none" stroke="var(--nav-icon)" stroke-width="5"/><g stroke="var(--nav-icon)" stroke-width="6" stroke-linecap="round"><path d="M26 4 V9 M26 43 V48 M4 26 H9 M43 26 H48 M10.4 10.4 L14 14 M38 38 L41.6 41.6 M41.6 10.4 L38 14 M14 38 L10.4 41.6"/></g></svg>
  </nav>
</main>
</body>
</html>
```